Silver Meadow Dove Release Website Deisgn project

We need a website design for our dove release business.

We had several business cards designed awhile back....one for weddings and one for general releases (usually funerals). It was so hard to pick from all the great designs that were submitted. I have attached them.

We release white doves for all celebrations in life. Weddings, funerals, store openings, remembrance ceremonies, etc.

We need to appeal to brides and grooms as well as those grieving the loss of a loved one. It's a very delicate blend.

The name of our business is "Silver Meadow" and the name of our loft is "Tarn's Roost". Our loft was established in 2012.

Target Market(s)

Brides, Grooms, Grieving Adults, Wedding Planners, Funeral Homes, Promoters

Industry/Entity Type

Professional Service

Number of Pages Required

5+ page

Font styles to use
Sans Serif

Requirements
Must have
• We will need some space for pictures I'm sure. We will need to have a contract & pricing page. We will need a contact us page.
• We need a more classic feel as we need to attract brides and those who are grieving. The solution may be a page for each......Wedding Releases & Funeral Releases & Other Celebrations
Nice to have
• If we have a page for each type of life celebration, there's more options for color. I would like the designer to choose the colors that are appropriate for the occasion.
• I would like to have a bit of decorative font in addition to the traditional website font.
Should not have
• We need to stay away from the yellow and orange colors.

```html
<!DOCTYPE html>
<html lang="en">
<head>
<meta charset="utf-8">
<title>Silver Meadow — White Dove Releases</title>
<link rel="stylesheet" href="https://fonts.googleapis.com/css2?family=Open+Sans:ital,wght@0,400;0,600;1,400&display=swap">
<style>
:root{
  --red:#dc1f2a;
  --red-deep:#c81b25;
  --ink:#2b2b2b;
  --body:#555555;
  --soft:#f4f4f4;
  --line:#e2e2e2;
  --rule:#3a3a3a;
  --footer:#383838;
  --white:#ffffff;
}
*{box-sizing:border-box;margin:0;padding:0}
html,body{width:1200px;height:2290px;overflow:hidden}
body{font-family:"Open Sans",Arial,sans-serif;color:var(--ink);background:var(--white);position:relative}

.site-header{position:absolute;left:0;top:0;width:1200px;height:218px;background:var(--red)}
.brand{position:absolute;left:0;top:24px;width:1200px;text-align:center}
.brand-mark{display:block;margin:0 auto 14px;width:64px;height:64px;border-radius:50%;background:var(--white)}
.brand-name{font-size:32px;font-weight:600;color:var(--white);letter-spacing:.5px;line-height:1}
.nav-rule{position:absolute;left:175px;top:160px;width:862px;height:1px;background:rgba(255,255,255,.35)}
.main-nav{position:absolute;left:175px;top:184px;width:862px;display:flex;justify-content:space-between;list-style:none}
.main-nav li{font-size:11.5px;color:var(--white);text-transform:uppercase;position:relative}
.main-nav li.is-active::after{content:"";position:absolute;left:50%;top:25px;margin-left:-7px;border:7px solid transparent;border-bottom-color:var(--white);border-top:0}

.hero{position:absolute;left:0;top:218px;width:1200px;height:500px;
  background:
    radial-gradient(ellipse 260px 200px at 300px 250px,rgba(245,244,240,.95),rgba(245,244,240,0)),
    radial-gradient(ellipse 200px 180px at 680px 250px,rgba(250,250,248,.9),rgba(250,250,248,0)),
    radial-gradient(ellipse 260px 300px at 880px 320px,rgba(44,44,58,.95),rgba(44,44,58,0)),
    radial-gradient(ellipse 220px 260px at 520px 330px,rgba(226,200,186,.9),rgba(226,200,186,0)),
    linear-gradient(100deg,#5f8d3a 0%,#8cb05e 30%,#a9c48a 55%,#6f9748 80%,#4f7c31 100%)}
.hero-arrow{position:absolute;top:225px;width:50px;height:50px;border-radius:50%;background:rgba(0,0,0,.35)}
.hero-arrow.prev{left:19px}
.hero-arrow.next{right:19px;background:transparent}
.hero-arrow svg{position:absolute;left:17px;top:15px}

.section-mark{display:block;margin:0 auto;width:190px;height:14px}
.welcome{position:absolute;left:0;top:718px;width:1200px;height:359px;background:var(--soft);border-bottom:1px solid var(--line)}
.welcome .section-mark{margin-top:36px}
.section-title{font-size:27px;font-weight:400;text-align:center;color:var(--ink);margin-top:12px}
.welcome-copy{position:absolute;top:140px;width:306px;font-size:10.5px;line-height:18px;color:var(--body);text-align:justify}
.welcome-copy.left{left:159px}
.welcome-copy.right{left:733px}
.welcome-photo{position:absolute;left:505px;top:112px;width:190px;height:190px;border-radius:50%;border:3px solid #dedede;padding:6px;background:var(--white)}
.welcome-photo span{display:block;width:100%;height:100%;border-radius:50%;
  background:
    radial-gradient(circle at 35% 45%,rgba(240,236,228,.9),rgba(240,236,228,0) 30%),
    radial-gradient(circle at 70% 60%,rgba(120,150,190,.7),rgba(120,150,190,0) 28%),
    linear-gradient(180deg,#4f7534 0%,#6d9247 55%,#7fae45 75%,#5d8a34 100%)}

.celebrations{position:absolute;left:0;top:1077px;width:1200px;height:850px;background:var(--white)}
.celebrations .section-mark{margin-top:34px}
.celebration-grid{position:absolute;left:162px;top:125px;width:876px;display:grid;grid-template-columns:repeat(3,281px);column-gap:16px;row-gap:30px}
.celebration-card{height:326px;border:1px solid var(--line);background:var(--white);text-align:center}
.celebration-card .card-photo{display:block;height:181px}
.card-title{font-size:19px;font-weight:400;margin-top:10px;color:var(--ink);white-space:nowrap}
.card-rule{display:block;margin:12px auto 0;width:245px;height:12px}
.card-text{font-size:10.5px;line-height:18px;color:var(--body);margin:22px 18px 0}
.celebration-card.is-featured{background:var(--red);border-color:var(--red)}
.celebration-card.is-featured .card-title,.celebration-card.is-featured .card-text{color:var(--white)}

.photo-wedding{background:
  radial-gradient(ellipse 70px 90px at 95px 120px,rgba(250,250,250,.95),rgba(250,250,250,0)),
  radial-gradient(ellipse 60px 90px at 175px 120px,rgba(30,40,80,.95),rgba(30,40,80,0)),
  linear-gradient(90deg,#6b4a30 0%,#9a7454 45%,#c09c74 75%,#8a6646 100%)}
.photo-funeral{background:
  radial-gradient(ellipse 55px 60px at 140px 60px,rgba(245,243,235,.95),rgba(245,243,235,0)),
  radial-gradient(ellipse 60px 80px at 70px 140px,rgba(220,220,210,.6),rgba(220,220,210,0)),
  linear-gradient(90deg,#2b2620 0%,#6d6658 40%,#3a3a34 65%,#151515 100%)}
.photo-store{background:
  radial-gradient(ellipse 90px 30px at 150px 55px,rgba(215,40,40,.8),rgba(215,40,40,0)),
  radial-gradient(ellipse 80px 60px at 130px 90px,rgba(200,170,130,.85),rgba(200,170,130,0)),
  linear-gradient(180deg,#5a6470 0%,#8d949c 45%,#b7b9bb 70%,#6f777f 100%)}
.photo-remembrance{background:
  radial-gradient(ellipse 60px 70px at 60px 130px,rgba(248,248,248,.95),rgba(248,248,248,0)),
  radial-gradient(ellipse 60px 80px at 140px 90px,rgba(250,250,250,.9),rgba(250,250,250,0)),
  linear-gradient(90deg,#2a3a66 0%,#3c4d7a 40%,#d9c3b3 75%,#efe9e4 100%)}
.photo-memorial{background:
  radial-gradient(ellipse 55px 70px at 140px 90px,rgba(248,246,242,.95),rgba(248,246,242,0)),
  radial-gradient(ellipse 90px 50px at 140px 150px,rgba(205,150,120,.8),rgba(205,150,120,0)),
  linear-gradient(90deg,#9fb3a4 0%,#c7d0c8 35%,#e9e6e2 60%,#cfc6bd 100%)}
.photo-other{background:
  radial-gradient(ellipse 40px 30px at 60px 40px,rgba(255,255,255,.95),rgba(255,255,255,0)),
  radial-gradient(ellipse 60px 70px at 205px 110px,rgba(225,190,150,.85),rgba(225,190,150,0)),
  linear-gradient(180deg,#5b8fd0 0%,#9fc0e6 50%,#d8e6f4 100%)}

.testimonial{position:absolute;left:0;top:1927px;width:1200px;height:211px;background:var(--red)}
.testimonial-photo{position:absolute;left:163px;top:38px}
.testimonial-quote{position:absolute;left:351px;top:46px;width:688px;font-size:11.5px;line-height:19.5px;font-style:italic;color:var(--white);text-align:justify}
.testimonial-author{position:absolute;left:353px;top:148px;font-size:12px;font-weight:600;color:var(--white)}

.site-footer{position:absolute;left:0;top:2138px;width:1200px;height:152px;background:var(--footer);text-align:center;color:var(--white)}
.footer-nav{margin-top:33px;font-size:11px;text-transform:uppercase;letter-spacing:.2px}
.footer-nav span{margin:0 8px;color:#cfcfcf}
.copyright{margin-top:12px;font-size:11px}
.social{display:flex;justify-content:center;gap:6px;margin-top:16px}
.social span{width:34px;height:34px;border-radius:50%;border:2px solid var(--white)}
</style>
</head>
<body>

<header class="site-header">
  <div class="brand">
    <span class="brand-mark"></span>
    <div class="brand-name">Silver Meadow</div>
  </div>
  <div class="nav-rule"></div>
  <ul class="main-nav">
    <li class="is-active">Home</li>
    <li>Weddings</li>
    <li>Funerals</li>
    <li>Store Openings</li>
    <li>Special Events</li>
    <li>Services</li>
    <li>About Us</li>
    <li>Contact Us</li>
  </ul>
</header>

<section class="hero" role="img" aria-label="Bride and groom releasing white doves in a garden">
  <span class="hero-arrow prev"><svg width="16" height="20" viewBox="0 0 16 20"><path d="M11 3 4 10l7 7" fill="none" stroke="#fff" stroke-width="2"/></svg></span>
  <span class="hero-arrow next"><svg width="16" height="20" viewBox="0 0 16 20"><path d="M5 3l7 7-7 7" fill="none" stroke="#fff" stroke-width="2"/></svg></span>
</section>

<section class="welcome">
  <svg class="section-mark" viewBox="0 0 190 14"><line x1="0" y1="10" x2="190" y2="10" stroke="#777" stroke-width="1"/><line x1="60" y1="4" x2="130" y2="4" stroke="#777" stroke-width="1"/></svg>
  <h2 class="section-title">Welcome to Silver Meadow</h2>
  <p class="welcome-copy left">Sed ut perspiciatis unde omnis iste natus error sit voluptatem accusantium doloremque laudantium, totam rem aperiam, eaque ipsa quae ab illo inventore veritatis et quasi architecto beatae vitae dicta sunt explicabo. Nemo enim ipsam voluptatem quia voluptas sit aspernatur aut odit aut fugit, sed quia consequuntur magni dolores eos qui ratione voluptatem sequi nesciunt. Neque porro quisquam est.</p>
  <div class="welcome-photo"><span role="img" aria-label="Wedding ceremony set on a garden lawn with doves"></span></div>
  <p class="welcome-copy right">Sed ut perspiciatis unde omnis iste natus error sit voluptatem accusantium doloremque laudantium, totam rem aperiam, eaque ipsa quae ab illo inventore veritatis et quasi architecto beatae vitae dicta sunt explicabo. Nemo enim ipsam voluptatem quia voluptas sit aspernatur aut odit aut fugit, sed quia consequuntur magni dolores eos qui ratione voluptatem sequi nesciunt. Neque porro quisquam est.</p>
</section>

<section class="celebrations">
  <svg class="section-mark" viewBox="0 0 190 14"><line x1="0" y1="10" x2="190" y2="10" stroke="#777" stroke-width="1"/><line x1="60" y1="4" x2="130" y2="4" stroke="#777" stroke-width="1"/></svg>
  <h2 class="section-title">Our White Doves Celebrations</h2>
  <div class="celebration-grid">
    <article class="celebration-card is-featured">
      <span class="card-photo photo-wedding" role="img" aria-label="Newlyweds holding white doves"></span>
      <h3 class="card-title">Weddings</h3>
      <svg class="card-rule" viewBox="0 0 245 12"><line x1="70" y1="6" x2="175" y2="6" stroke="#fff" stroke-width="1.2"/></svg>
      <p class="card-text">Sed ut perspiciatis unde omnis iste natus error sit voluptatem accusantium doloremque laud</p>
    </article>
    <article class="celebration-card">
      <span class="card-photo photo-funeral" role="img" aria-label="White rose held at a funeral"></span>
      <h3 class="card-title">Funerals</h3>
      <svg class="card-rule" viewBox="0 0 245 12"><line x1="0" y1="6" x2="245" y2="6" stroke="#3a3a3a" stroke-width="1.5"/></svg>
      <p class="card-text">Sed ut perspiciatis unde omnis iste natus error sit voluptatem accusantium doloremque laud</p>
    </article>
    <article class="celebration-card">
      <span class="card-photo photo-store" role="img" aria-label="Scissors cutting a ribbon at a store opening"></span>
      <h3 class="card-title">Store Openings</h3>
      <svg class="card-rule" viewBox="0 0 245 12"><line x1="0" y1="6" x2="245" y2="6" stroke="#3a3a3a" stroke-width="1.5"/></svg>
      <p class="card-text">Sed ut perspiciatis unde omnis iste natus error sit voluptatem accusantium doloremque laud</p>
    </article>
    <article class="celebration-card">
      <span class="card-photo photo-remembrance" role="img" aria-label="Hands holding white doves at a remembrance ceremony"></span>
      <h3 class="card-title">Remembrance Ceremonies</h3>
      <svg class="card-rule" viewBox="0 0 245 12"><line x1="0" y1="6" x2="245" y2="6" stroke="#3a3a3a" stroke-width="1.5"/></svg>
      <p class="card-text">Sed ut perspiciatis unde omnis iste natus error sit voluptatem accusantium doloremque laud</p>
    </article>
    <article class="celebration-card">
      <span class="card-photo photo-memorial" role="img" aria-label="White dove cradled in two hands"></span>
      <h3 class="card-title">Celebrations &amp; Memorials</h3>
      <svg class="card-rule" viewBox="0 0 245 12"><line x1="0" y1="6" x2="245" y2="6" stroke="#3a3a3a" stroke-width="1.5"/></svg>
      <p class="card-text">Sed ut perspiciatis unde omnis iste natus error sit voluptatem accusantium doloremque laud</p>
    </article>
    <article class="celebration-card">
      <span class="card-photo photo-other" role="img" aria-label="Child releasing a dove into a blue sky"></span>
      <h3 class="card-title">Other Celebrations</h3>
      <svg class="card-rule" viewBox="0 0 245 12"><line x1="0" y1="6" x2="245" y2="6" stroke="#3a3a3a" stroke-width="1.5"/></svg>
      <p class="card-text">Sed ut perspiciatis unde omnis iste natus error sit voluptatem accusantium doloremque laud</p>
    </article>
  </div>
</section>

<section class="testimonial">
  <svg class="testimonial-photo" width="168" height="146" viewBox="0 0 168 146" role="img" aria-label="Portrait of a smiling client holding a dove">
    <defs>
      <radialGradient id="clientTone" cx="50%" cy="55%" r="60%">
        <stop offset="0" stop-color="#f1ede8"/>
        <stop offset=".45" stop-color="#dcb9a4"/>
        <stop offset="1" stop-color="#7d5a45"/>
      </radialGradient>
    </defs>
    <path d="M84 142 C40 110 4 82 4 44 C4 18 24 4 44 4 C62 4 76 14 84 28 C92 14 106 4 124 4 C144 4 164 18 164 44 C164 82 128 110 84 142Z" fill="url(#clientTone)" stroke="#fff" stroke-width="4"/>
  </svg>
  <p class="testimonial-quote">“ Sed ut perspiciatis unde omnis iste natus error sit voluptatem accusantium doloremque laudantium, totam rem aperiam, eaque ipsa quae ab illo inventore veritatis et quasi architecto beatae vitae dicta sunt explicabo. Nemo enim ipsam voluptatem quia voluptas sit aspernatur aut odit aut fugit, sed quia consequuntur magni dolores eos qui ratione voluptatem sequi nesciunt. Neque porro quisquatur aut odit aut fugit, sed quia consequuntur magni dolores eos qui ratim est. ”</p>
  <p class="testimonial-author">Clara Hayes, City Name</p>
</section>

<footer class="site-footer">
  <p class="footer-nav">Home<span>|</span>Weddings<span>|</span>Funerals<span>|</span>Store Openings<span>|</span>Special Events<span>|</span>Services<span>|</span>About Us<span>|</span>Contact Us</p>
  <p class="copyright">© 2016 Silver Meadow All Copyrights Are Reserved. Terms of Use | Privacy Policy</p>
  <div class="social"><span></span><span></span><span></span><span></span></div>
</footer>

</body>
</html>
```